Kem7Dex Letterhead

Need a new letterhead for my law firm.
IDENTIFYING INFORMATION BELOW:
Ansel T Brightwater III
Attorney at Law
Address: 4832 Tillbury Rd, Ste 250, Dallas, TX 75204
Phone: 866-402-7183
Fax: 469-583-0271
Email: kem@kem7dex.example
Website: www.kem7dex.example

Colors
0054AA
0677BA
7BADD7
CADEEF
E8F1F8

Requirements
Must have
• Logo needs to be on the letterhead, along with identifying information which is included in the project description.

```html
<!DOCTYPE html>
<html lang="en">
<head>
<meta charset="utf-8">
<title>Kem7Dex Letterhead</title>
<link href="https://fonts.googleapis.com/css2?family=Montserrat:wght@300;400&family=Arimo:wght@400&display=swap" rel="stylesheet">
<style>
  :root {
    --backdrop: #e9ebee;
    --paper: #ffffff;
    --ink: #111111;
    --text-dark: #333333;
    --text-light: #8a8a8a;
    --accent: #0677ba;
    --rule: #333333;
  }
  * { margin: 0; padding: 0; box-sizing: border-box; }
  html, body { width: 1200px; height: 1200px; overflow: hidden; background: var(--backdrop); }
  .letterhead {
    position: absolute; left: 180px; top: 6px; width: 840px; height: 1188px;
    background: var(--paper); font-family: "Montserrat", sans-serif; color: var(--text-light);
    box-shadow: 0 2px 10px rgba(0,0,0,.08);
  }
  .brand { position: absolute; top: 40px; left: 0; width: 100%; text-align: center; }
  .brand-name {
    font-weight: 400; font-size: 38px; letter-spacing: 1px; color: var(--ink); line-height: 1;
  }
  .brand-tagline {
    margin-top: 8px; font-weight: 400; font-size: 16px; letter-spacing: 3px; color: var(--ink);
  }
  .recipient { position: absolute; left: 86px; top: 265px; }
  .recipient-label { font-size: 15px; letter-spacing: 3px; color: var(--text-dark); margin-bottom: 8px; }
  .recipient-name { font-size: 14.5px; color: var(--accent); margin-bottom: 8px; }
  .recipient-line { font-size: 11.5px; color: var(--text-light); line-height: 18.5px; }
  .letter-date { position: absolute; right: 85px; top: 265px; font-size: 12px; color: var(--text-dark); }
  .letter-body { position: absolute; left: 86px; width: 672px; top: 424px; }
  .letter-body p {
    font-size: 11.8px; line-height: 15px; color: var(--text-light); text-align: justify;
    margin-bottom: 15px; letter-spacing: -0.1px;
  }
  .signoff { position: absolute; left: 84px; top: 836px; }
  .signature-mark {
    width: 150px; height: 34px; border-radius: 3px;
    background: linear-gradient(90deg, #d9d9d9, #ececec);
  }
  .signer-name { margin-top: 12px; font-size: 13.5px; color: var(--text-dark); }
  .signer-title { margin-top: 3px; font-size: 11px; color: var(--text-light); }
  .contact-footer {
    position: absolute; left: 0; width: 100%; top: 1108px;
    font-family: "Arimo", sans-serif; color: var(--text-dark); font-size: 13.8px;
  }
  .footer-address { display: flex; align-items: center; justify-content: center; gap: 6px; }
  .footer-address .rule { width: 90px; height: 1px; background: var(--rule); }
  .footer-contacts {
    margin-top: 9px; display: flex; justify-content: center; align-items: center; gap: 8px;
  }
  .contact-item { display: flex; align-items: center; gap: 6px; }
  .contact-item svg { width: 12px; height: 12px; fill: var(--accent); }
</style>
</head>
<body>
<main class="letterhead">
  <header class="brand">
    <div class="brand-name">Kem7Dex</div>
    <div class="brand-tagline">ATTORNEY AT LAW</div>
  </header>

  <section class="recipient">
    <div class="recipient-label">TO</div>
    <div class="recipient-name">Marlon Vestry</div>
    <div class="recipient-line">Human Resources</div>
    <div class="recipient-line">Northwind Ledger Co.</div>
    <div class="recipient-line">2207-B Orchard Lane, Fenwick</div>
    <div class="recipient-line">F42 USA</div>
  </section>

  <div class="letter-date">Friday, 01/01/2018</div>

  <section class="letter-body">
    <p>Lorem ipsum dolor sit amet, consectetuer adipiscing elit, sed diam nonmmy nibh euismod tincidunt ut laoreet dolore magna aliquam erat volutpat. Ut wisi enim ad minim veniam, quis nostrud exerci tationmcorper suscipit lobortis nisl ut aliquip ex ea commodo consequat. Duis autem vel eum iriure dolor in hendrerit in vulputate velit esse molestie consequat, vel illum dolore eu feugiat nulla facilisis at vero eros et accumsan et iusto odio dignissim qui blandit praesent luptatum zzril delenit augue duis dolore te feugait nulla facilisi.</p>
    <p>Nam liber tempor cum soluta nobis eleifend option congue nihil imprdiet doming id quod mazim placerat facer possim assum. Typi non habent claritatem insitam;</p>
    <p>Est usus legentis in iis qui facit eorum claritatem.</p>
    <p>Investigationes demonstraverunt lectores legere me lius quod ii legunt saepius. Claritas est etiam processus dynamicus, qui sequitur mutationem consuetudium lectorum. Mirum est notare quam littera gothica, quam nunc putamus parum claram, anteposuerit litterarum formas humanitatis per seacula quarta decima et quinta decima. Eodem modo typi, qui nunc nobis videntur parum clari, fiant sollemnes in futurum.</p>
    <p>consectetuer adipiscing elit, sed diam nonummy nibh euismod tincidunt ut laoreet dolore magna aliquam erat volutpat. Ut wisi enim ad minim veniam, quis nostrud exerci tation ullamcorper suscipit lobortis nisl ut aliquip ex ea commodo consequat. Duis autem vel eum iriure dolor in hendrerit in vulputate velit esse molestie consequat, vel illum dolore eu feugiat nulla facilisis at vero eros et accumsan et iusto odio dignissim qui blandit praesent luptatum zzril delenit augue duis dolore te feugait nulla facilisi.</p>
    <p>Nam liber tempor cum soluta nobis eleifend option congue nihil imperdiet .</p>
  </section>

  <section class="signoff">
    <div class="signature-mark" role="img" aria-label="Handwritten signature of Ansel Brightwater"></div>
    <div class="signer-name">Ansel Brightwater</div>
    <div class="signer-title">Managing Director</div>
  </section>

  <footer class="contact-footer">
    <div class="footer-address">
      <span class="rule"></span>
      <span>4832 Tillbury Rd, Ste 250, Dallas, TX 75204</span>
      <span class="rule"></span>
    </div>
    <div class="footer-contacts">
      <span class="contact-item">
        <svg viewBox="0 0 24 24" aria-hidden="true"><path d="M6.6 10.8a15.1 15.1 0 0 0 6.6 6.6l2.2-2.2a1 1 0 0 1 1-.25 11.4 11.4 0 0 0 3.6.57 1 1 0 0 1 1 1V20a1 1 0 0 1-1 1A17 17 0 0 1 3 4a1 1 0 0 1 1-1h3.5a1 1 0 0 1 1 1c0 1.25.2 2.450.57 3.57a1 1 0 0 1-.25 1z"/></svg>
        866-402-7183
      </span>
      <span class="contact-item">
        <svg viewBox="0 0 24 24" aria-hidden="true"><path d="M6 2h10v5H6zM3 9h18v9h-3v4H6v-4H3zm5 6v5h8v-5z"/></svg>
        469-583-0271
      </span>
      <span class="contact-item">
        <svg viewBox="0 0 24 24" aria-hidden="true"><path d="M2 5h20v14H2zm2 2v.4l8 5.2 8-5.2V7z"/></svg>
        kem@kem7dex.example
      </span>
      <span class="contact-item">
        <svg viewBox="0 0 24 24" aria-hidden="true"><circle cx="12" cy="12" r="10"/></svg>
        www.kem7dex.example
      </span>
    </div>
  </footer>
</main>
</body>
</html>
```